Innovative label design for premium vodka bottle

We are looking for a bottle design (with logo) for a new premium vodka company based in Uganda. We are the first company to produce a premium vodka in Uganda made exclusively with local ingredients. We want the label design to set us apart from the more traditional (read boring) designs of local packaging and bring raise the bar for Ugandan packaging design.

We will initially sell to local markets and hope to go global in two years. The vodka is called "IRONCREST" after the famous adult mountain gorillas which live in the mountains of western Uganda.

The bottle design has to be simple and appealing to both an Africana and an International consumer (tourists). Simple, clean and to the point. The main color should be green and can or cannot include a rendering of a gorilla. Silver must also be included in the design (could be printed on metallic paper). It also can include the mountain landscapes of western Uganda. But please we are also open to more creative ideas which stray from these typical images of Uganda. I will attach some images of the silverback, the mountains of Uganda and other labels of local alcoholic beverages. Must be printed on paper. Can be glossy, matte or metallic. Do not submit ideas for labels printing on transparent film.

The size of the label should be 75mm wide by 120mm high. Also attached is an image of the bottle to be used.

Text that MUST be on the label:

Ironcrest
Ultra-Premium Vodka
Produced in Uganda
Triple Distilled from Sugar Cane
42.5%ABV
700ML

Text that CAN be incorporated:
Purely Ugandan
Triple Distilled-Ten Times filtered
3X Distilled - 10X Filtered

Please feel free to contact me with any inquiries.
Updates

Project Deadline Extended
Reason: Since we cannot meet until Wednesday to consider the designs, may as well allow the crowd a couple more days of creativity. Cheers, Bram

Hi,

Thank you all for your updates. We are currently ging through the designs and hope to have a decision made by the end of the week.

Well done!

Cheers,

Bram

Target Market(s)

Upmarket Ugandans and International consumers

Industry/Entity Type

Adult

Requirements
Must have
• Must be printed on paper. Can be glossy, matte or metallic. Do not submit ideas for labels printing on transparent film.

```html
<!DOCTYPE html>
<html lang="en">
<head>
<meta charset="utf-8">
<title>Ironcrest Ultra-Premium Vodka – Label Options</title>
<link rel="stylesheet" href="https://fonts.googleapis.com/css2?family=Tinos:wght@400;700&display=swap">
<style>
  :root {
    --page: #ffffff;
    --frame: #c9c9c9;
    --forest: #0f2a1c;
    --ink: #1d2a22;
    --silver-light: #f6f6f6;
    --silver-mid: #d2d2d2;
    --silver-dark: #a9a9a9;
    --rim: #8f8f8f;
    --white: #ffffff;
    --emblem: #5d6b62;
  }
  html, body {
    margin: 0;
    padding: 0;
    width: 1200px;
    height: 1000px;
    overflow: hidden;
    background: var(--page);
  }
  .canvas {
    position: relative;
    width: 1198px;
    height: 998px;
    border: 1px solid var(--frame);
    background: var(--page);
  }
  .label {
    position: absolute;
    width: 345px;
    height: 315px;
  }
  .label--green  { left: 52px;  top: 344px; }
  .label--white  { left: 430px; top: 344px; }
  .label--accent { left: 820px; top: 339px; }
  .label svg { display: block; overflow: visible; }
  .brand {
    font-family: "Tinos", "Times New Roman", serif;
    font-weight: 700;
    font-size: 39px;
    letter-spacing: 0.5px;
  }
  .subtitle {
    font-family: "Tinos", "Times New Roman", serif;
    font-size: 14.5px;
    letter-spacing: 0.3px;
  }
  .detail {
    font-family: "Tinos", "Times New Roman", serif;
    font-size: 11px;
    fill: var(--ink);
  }
  .volume {
    font-family: "Tinos", "Times New Roman", serif;
    font-size: 8.5px;
    fill: var(--ink);
  }
  .rule { stroke: var(--forest); stroke-width: 1; }
  .rule--light { stroke: var(--white); stroke-width: 1; }
</style>
</head>
<body>
<div class="canvas">
  <svg width="0" height="0" style="position:absolute" aria-hidden="true">
    <defs>
      <linearGradient id="metal" x1="0" y1="0" x2="1" y2="1">
        <stop offset="0" stop-color="#c4c4c4"/>
        <stop offset="0.35" stop-color="#f2f2f2"/>
        <stop offset="0.55" stop-color="#cfcfcf"/>
        <stop offset="0.8" stop-color="#f0f0f0"/>
        <stop offset="1" stop-color="#b5b5b5"/>
      </linearGradient>
      <linearGradient id="rimGrad" x1="0" y1="0" x2="1" y2="1">
        <stop offset="0" stop-color="#e9e9e9"/>
        <stop offset="0.5" stop-color="#9a9a9a"/>
        <stop offset="1" stop-color="#e2e2e2"/>
      </linearGradient>
    </defs>
  </svg>

  <!-- Label option 1: green wordmark -->
  <div class="label label--green">
    <svg width="345" height="315" viewBox="0 0 345 315">
      <path d="M172 3 C282 3 342 32 342 112 C342 205 232 312 172 312 C112 312 3 205 3 112 C3 32 62 3 172 3 Z" fill="url(#rimGrad)" stroke="var(--rim)" stroke-width="1"/>
      <path d="M172 10 C276 10 335 37 335 113 C335 201 228 305 172 305 C116 305 10 201 10 113 C10 37 68 10 172 10 Z" fill="url(#metal)" stroke="var(--white)" stroke-width="1.2"/>
      <line class="rule--light" x1="92" y1="47" x2="252" y2="47"/>
      <rect x="150" y="41" width="44" height="9" rx="4" fill="var(--silver-dark)" role="img" aria-label="Small silver flourish ornament"/>
      <text class="brand" x="172" y="94" text-anchor="middle" fill="var(--forest)">IRONCREST</text>
      <line class="rule--light" x1="92" y1="110" x2="252" y2="110"/>
      <rect x="150" y="105" width="44" height="9" rx="4" fill="var(--silver-dark)" role="img" aria-label="Small silver flourish ornament"/>
      <text class="subtitle" x="172" y="138" text-anchor="middle" fill="var(--white)">ULTRA-PREMIUM VODKA</text>
      <rect x="108" y="152" width="128" height="46" rx="20" fill="var(--emblem)" opacity="0.55" role="img" aria-label="Emblem: mountain gorilla in an oval framed by scrollwork"/>
      <line class="rule" x1="130" y1="205" x2="214" y2="205" stroke-opacity="0.5"/>
      <text class="detail" x="172" y="225" text-anchor="middle">Produced in Uganda</text>
      <text class="detail" x="172" y="243" text-anchor="middle">Triple Distilled from Sugar Cane</text>
      <text class="volume" x="172" y="275" text-anchor="middle">42.5%ABV</text>
      <text class="volume" x="172" y="288" text-anchor="middle">700ML</text>
    </svg>
  </div>

  <!-- Label option 2: white wordmark, dark rules -->
  <div class="label label--white">
    <svg width="345" height="315" viewBox="0 0 345 315">
      <path d="M172 3 C282 3 342 32 342 112 C342 205 232 312 172 312 C112 312 3 205 3 112 C3 32 62 3 172 3 Z" fill="url(#rimGrad)" stroke="var(--rim)" stroke-width="1"/>
      <path d="M172 10 C276 10 335 37 335 113 C335 201 228 305 172 305 C116 305 10 201 10 113 C10 37 68 10 172 10 Z" fill="url(#metal)" stroke="var(--white)" stroke-width="1.2"/>
      <line class="rule" x1="72" y1="47" x2="272" y2="47"/>
      <rect x="150" y="41" width="44" height="9" rx="4" fill="var(--forest)" role="img" aria-label="Small green flourish ornament"/>
      <text class="brand" x="172" y="94" text-anchor="middle" fill="var(--white)">IRONCREST</text>
      <line class="rule" x1="72" y1="110" x2="272" y2="110"/>
      <rect x="150" y="105" width="44" height="9" rx="4" fill="var(--forest)" role="img" aria-label="Small green flourish ornament"/>
      <text class="subtitle" x="172" y="138" text-anchor="middle" fill="var(--ink)">ULTRA-PREMIUM VODKA</text>
      <rect x="108" y="152" width="128" height="46" rx="20" fill="var(--silver-light)" stroke="var(--silver-dark)" stroke-width="0.8" role="img" aria-label="Emblem: mountain gorilla in an oval framed by scrollwork"/>
      <line class="rule" x1="130" y1="205" x2="214" y2="205" stroke-opacity="0.5"/>
      <text class="detail" x="172" y="225" text-anchor="middle">Produced in Uganda</text>
      <text class="detail" x="172" y="243" text-anchor="middle">Triple Distilled from Sugar Cane</text>
      <text class="volume" x="172" y="275" text-anchor="middle">42.5%ABV</text>
      <text class="volume" x="172" y="288" text-anchor="middle">700ML</text>
    </svg>
  </div>

  <!-- Label option 3: white wordmark, green emblem -->
  <div class="label label--accent">
    <svg width="345" height="315" viewBox="0 0 345 315">
      <path d="M172 3 C282 3 342 32 342 112 C342 205 232 312 172 312 C112 312 3 205 3 112 C3 32 62 3 172 3 Z" fill="url(#rimGrad)" stroke="var(--rim)" stroke-width="1"/>
      <path d="M172 10 C276 10 335 37 335 113 C335 201 228 305 172 305 C116 305 10 201 10 113 C10 37 68 10 172 10 Z" fill="url(#metal)" stroke="var(--white)" stroke-width="1.2"/>
      <line class="rule" x1="72" y1="47" x2="272" y2="47"/>
      <rect x="150" y="41" width="44" height="9" rx="4" fill="var(--forest)" role="img" aria-label="Small green flourish ornament"/>
      <text class="brand" x="172" y="94" text-anchor="middle" fill="var(--white)">IRONCREST</text>
      <line class="rule" x1="72" y1="110" x2="272" y2="110"/>
      <rect x="150" y="105" width="44" height="9" rx="4" fill="var(--forest)" role="img" aria-label="Small green flourish ornament"/>
      <text class="subtitle" x="172" y="138" text-anchor="middle" fill="var(--ink)">ULTRA-PREMIUM VODKA</text>
      <rect x="108" y="152" width="128" height="46" rx="20" fill="var(--emblem)" opacity="0.55" role="img" aria-label="Emblem: mountain gorilla in an oval framed by scrollwork"/>
      <line class="rule" x1="130" y1="205" x2="214" y2="205" stroke-opacity="0.5"/>
      <text class="detail" x="172" y="225" text-anchor="middle">Produced in Uganda</text>
      <text class="detail" x="172" y="243" text-anchor="middle">Triple Distilled from Sugar Cane</text>
      <text class="volume" x="172" y="275" text-anchor="middle">42.5%ABV</text>
      <text class="volume" x="172" y="288" text-anchor="middle">700ML</text>
    </svg>
  </div>
</div>
</body>
</html>
```